Lume Hart Co Need a custom graphic

I need to have the attached chart re-designed in a hand colored pencil format. The heading needs to be changed to "The most effective methods for hiring sales people". Do not include the background logo in the sample file.

Place the attached Lume Hart Co logo next to the most effective methods (91%)

```html
<!DOCTYPE html>
<html lang="en">
<head>
<meta charset="utf-8">
<title>The most effective methods for hiring sales people</title>
<link href="https://fonts.googleapis.com/css2?family=Patrick+Hand&family=Gochi+Hand&family=Permanent+Marker&display=swap" rel="stylesheet">
<style>
  :root {
    --page: #ffffff;
    --grid: #bdbdbd;
    --ink: #1c1c1c;
    --navy: #2a2d4a;
    --pencil-red: #b83a26;
    --band: #2f2f2f;
    --logo-blue: #2f6fb3;
  }
  html, body {
    margin: 0;
    width: 1200px;
    height: 1200px;
    overflow: hidden;
    background: var(--page);
  }
  .chart-sheet {
    position: absolute;
    left: 0;
    top: 0;
    width: 1200px;
    height: 1200px;
  }
  .title-band { fill: var(--band); }
  .title-text {
    font-family: 'Permanent Marker', cursive;
    font-size: 34px;
    fill: #ffffff;
  }
  .grid-line { stroke: var(--grid); stroke-width: 2.5; fill: none; }
  .tick-label {
    font-family: 'Gochi Hand', cursive;
    font-size: 17px;
    fill: var(--ink);
  }
  .axis-title {
    font-family: 'Gochi Hand', cursive;
    font-size: 38px;
    fill: var(--ink);
    letter-spacing: 1px;
  }
  .trend-line { stroke: var(--pencil-red); stroke-width: 3; fill: none; stroke-linejoin: round; }
  .data-point { fill: var(--pencil-red); }
  .pointer { stroke: var(--pencil-red); stroke-width: 2.5; fill: none; stroke-linecap: round; }
  .pointer-head { fill: var(--pencil-red); }
  .method-pill {
    fill: #ffffff;
    stroke: var(--navy);
    stroke-width: 1.8;
    stroke-dasharray: 14 3 2 3;
  }
  .method-label {
    font-family: 'Patrick Hand', cursive;
    font-size: 17px;
    fill: var(--ink);
  }
  .brand-name {
    font-family: 'Patrick Hand', cursive;
    font-size: 30px;
    fill: var(--logo-blue);
  }
  .brand-mark { fill: var(--logo-blue); }
</style>
</head>
<body>
<svg class="chart-sheet" viewBox="0 0 1200 1200" xmlns="http://www.w3.org/2000/svg">
  <defs>
    <marker id="arrowhead" viewBox="0 0 10 10" refX="8" refY="5" markerWidth="7" markerHeight="7" orient="auto">
      <path class="pointer-head" d="M0,0 L10,5 L0,10 z"/>
    </marker>
  </defs>

  <!-- heading band -->
  <rect class="title-band" x="205" y="296" width="840" height="52" rx="3"/>
  <text class="title-text" x="625" y="334" text-anchor="middle">The most effective methods for hiring sales people</text>

  <!-- grid -->
  <g class="chart-grid">
    <path class="grid-line" d="M210 360 H1055 M210 418 H1055 M210 476 H1055 M210 533 H1055 M210 591 H1055 M210 648 H1055 M210 706 H1055 M210 763 H1055 M210 821 H1055 M210 878 H1055"/>
    <path class="grid-line" d="M210 352 V880 M285 352 V880 M362 352 V880 M435 352 V880 M512 352 V880 M588 352 V880 M662 352 V880 M735 352 V880 M812 352 V880 M890 352 V880 M968 352 V880 M1045 352 V880"/>
  </g>

  <!-- axis ticks -->
  <g class="y-ticks">
    <text class="tick-label" x="200" y="366" text-anchor="end">0.90</text>
    <text class="tick-label" x="200" y="424" text-anchor="end">0.80</text>
    <text class="tick-label" x="200" y="482" text-anchor="end">0.70</text>
    <text class="tick-label" x="200" y="539" text-anchor="end">0.60</text>
    <text class="tick-label" x="200" y="597" text-anchor="end">0.50</text>
    <text class="tick-label" x="200" y="654" text-anchor="end">0.40</text>
    <text class="tick-label" x="200" y="712" text-anchor="end">0.30</text>
    <text class="tick-label" x="200" y="769" text-anchor="end">0.20</text>
    <text class="tick-label" x="200" y="827" text-anchor="end">0.10</text>
    <text class="tick-label" x="200" y="884" text-anchor="end">0.00</text>
  </g>
  <text class="axis-title" transform="translate(145 592) rotate(-90)" text-anchor="middle">Predictive validity</text>
  <text class="axis-title" x="658" y="912" text-anchor="middle">Hiring Method</text>

  <!-- brand -->
  <g class="brand">
    <text class="brand-name" x="772" y="382">Lume Hart Co</text>
    <rect class="brand-mark" x="940" y="360" width="14" height="14"/>
  </g>

  <!-- trend -->
  <polyline class="trend-line" points="284,829 347,773 434,757 508,753 585,734 660,735 733,687 812,578 890,527 968,451 1018,359"/>
  <g class="data-points">
    <circle class="data-point" cx="284" cy="829" r="5"/>
    <circle class="data-point" cx="347" cy="773" r="4"/>
    <circle class="data-point" cx="434" cy="757" r="4"/>
    <circle class="data-point" cx="508" cy="753" r="4"/>
    <circle class="data-point" cx="585" cy="734" r="4"/>
    <circle class="data-point" cx="660" cy="735" r="4"/>
    <circle class="data-point" cx="733" cy="687" r="5"/>
    <circle class="data-point" cx="812" cy="578" r="4"/>
    <circle class="data-point" cx="890" cy="527" r="4"/>
    <circle class="data-point" cx="968" cy="451" r="4"/>
    <circle class="data-point" cx="1018" cy="359" r="4"/>
  </g>

  <!-- pointers -->
  <g class="pointers">
    <path class="pointer" marker-end="url(#arrowhead)" d="M310 855 L290 837"/>
    <path class="pointer" marker-end="url(#arrowhead)" d="M320 746 L342 766"/>
    <path class="pointer" marker-end="url(#arrowhead)" d="M408 706 L430 748"/>
    <path class="pointer" marker-end="url(#arrowhead)" d="M535 790 L515 763"/>
    <path class="pointer" marker-end="url(#arrowhead)" d="M588 660 L588 724"/>
    <path class="pointer" marker-end="url(#arrowhead)" d="M712 792 L686 762"/>
    <path class="pointer" marker-end="url(#arrowhead)" d="M755 716 L738 696"/>
    <path class="pointer" marker-end="url(#arrowhead)" d="M855 606 L818 588"/>
    <path class="pointer" marker-end="url(#arrowhead)" d="M820 540 L862 530"/>
    <path class="pointer" marker-end="url(#arrowhead)" d="M905 463 L958 452"/>
    <path class="pointer" marker-end="url(#arrowhead)" d="M982 402 L1010 380"/>
  </g>

  <!-- method labels -->
  <g class="method-labels">
    <rect class="method-pill" x="305" y="845" width="145" height="26" rx="13"/>
    <text class="method-label" x="312" y="864">Culture test, 13%</text>

    <rect class="method-pill" x="225" y="719" width="140" height="26" rx="13"/>
    <text class="method-label" x="237" y="738">Resume, 18%</text>

    <rect class="method-pill" x="300" y="670" width="265" height="27" rx="13"/>
    <text class="method-label" x="314" y="689">Behavior/personality test, 20%</text>

    <rect class="method-pill" x="405" y="792" width="207" height="26" rx="13"/>
    <text class="method-label" x="411" y="811">Traditional interview, 20%</text>

    <rect class="method-pill" x="518" y="624" width="190" height="27" rx="13"/>
    <text class="method-label" x="530" y="643">Reference check, 23 %</text>

    <rect class="method-pill" x="648" y="791" width="212" height="27" rx="13"/>
    <text class="method-label" x="652" y="810">Emotional intelligence, 23%</text>

    <rect class="method-pill" x="736" y="716" width="136" height="26" rx="13"/>
    <text class="method-label" x="743" y="735">Skills test, 33%</text>

    <rect class="method-pill" x="810" y="608" width="230" height="26" rx="13"/>
    <text class="method-label" x="816" y="627">General mental ability, 51%</text>

    <rect class="method-pill" x="438" y="541" width="377" height="26" rx="13"/>
    <text class="method-label" x="445" y="560">Highly structured interview with scorecard, 57%</text>

    <rect class="method-pill" x="604" y="471" width="291" height="26" rx="13"/>
    <text class="method-label" x="613" y="490">Multi-measurement assessment, 71%</text>

    <rect class="method-pill" x="573" y="404" width="407" height="26" rx="13"/>
    <text class="method-label" x="578" y="423">Sales-specific multi-measurement assessment, 91%</text>
  </g>
</svg>
</body>
</html>
```